Business Card Design Project

I am a psychotherapist, counselor and expressive arts therapist (means I use every art form imaginable in the service of healing). I'm just starting out in private practice in San Francisco, CA. I work with individual adults, children and families. I'd like the card to mirror the simplicity and color palate of my website. I also would love if there is a symbol, image of fire, flame or spark (that is warming, not frightening).

Check out my website: www.lorabecketmft.com

I want the cards to be printed in letter press so please keep that in mind!

Target Market(s)

Upper Middle Class Adults who are progressively minded, artistic or artists, open to psychotherapy, interested in health & healing.

Industry/Entity Type

Business

Requirements
Must have
• Text to be included:

Lora Becket
Counseling, Psychotherapy & Expressive Arts

2914 Alderwood Avenue, Suite D
San Francisco, CA 94127
p. 415.206.3791
lorajanebecket@meadowpost.net

www.lorabecketmft.com

MFT License Number 48671

It's OK to abbreviate Number to # or Street to St., etc.

Must be compatible with letter press printing.
Nice to have
• I don't have a logo. I don't expect designers to necessarily create one for me, but if someone comes up with a simple image (see above about flame), that would be great. I don't have much of a budget now, but expect that to change in the next year or so and then could buy a logo for my website, future letterhead, etc.

```html
<!DOCTYPE html>
<html lang="en">
<head>
<meta charset="utf-8">
<title>Lora Becket — Business Card</title>
<link rel="stylesheet" href="https://fonts.googleapis.com/css2?family=Exo+2:wght@400&display=swap">
<style>
  :root {
    --backdrop: #d6d6d6;
    --card: #ffffff;
    --crimson: #d2384f;
    --peach: #eea37f;
    --card-shadow: rgba(0, 0, 0, 0.18);
  }
  * { box-sizing: border-box; margin: 0; padding: 0; }
  html, body {
    width: 1200px;
    height: 900px;
    overflow: hidden;
    background: var(--backdrop);
    font-family: "Exo 2", sans-serif;
    color: var(--crimson);
  }
  .stage { position: relative; width: 1200px; height: 900px; }
  .card {
    position: absolute;
    top: 307px;
    width: 500px;
    height: 286px;
    background: var(--card);
    box-shadow: 0 6px 18px var(--card-shadow);
  }
  .card--front { left: 70px; }
  .card--back { left: 630px; }

  /* front: brand name where the mark sits */
  .brand {
    position: absolute;
    left: 50%;
    top: 90px;
    transform: translateX(-50%);
    display: flex;
    align-items: center;
    gap: 8px;
    font-size: 17px;
    font-weight: 400;
    white-space: nowrap;
  }
  .brand__dot {
    width: 12px;
    height: 12px;
    border-radius: 50%;
    background: var(--peach);
  }
  .front__tagline {
    position: absolute;
    left: 0;
    right: 0;
    top: 170px;
    text-align: center;
    font-size: 14px;
    letter-spacing: 0.2px;
  }

  /* back */
  .back__mark {
    position: absolute;
    left: 40px;
    top: 118px;
    width: 44px;
    height: 44px;
    border-radius: 50%;
    background: linear-gradient(160deg, var(--crimson), var(--peach));
    opacity: 0.85;
  }
  .back__accent {
    position: absolute;
    right: 0;
    top: 38px;
    width: 8px;
    height: 36px;
    background: var(--crimson);
  }
  .back__header {
    position: absolute;
    right: 32px;
    top: 34px;
    text-align: right;
  }
  .back__name {
    font-size: 24px;
    font-weight: 400;
    line-height: 1.1;
    letter-spacing: 0.4px;
  }
  .back__role { font-size: 11.5px; margin-top: 2px; }
  .back__contact {
    position: absolute;
    right: 22px;
    top: 140px;
    text-align: right;
    font-size: 14px;
    font-style: normal;
    line-height: 19px;
  }
  .contact__line {
    display: flex;
    justify-content: flex-end;
    align-items: center;
    gap: 6px;
  }
  .contact__icon { width: 10px; height: 10px; flex: none; }
  .contact__icon--blank { visibility: hidden; }
  .contact__license { margin-top: 4px; }
</style>
</head>
<body>
<main class="stage">
  <section class="card card--front" aria-label="Card front">
    <div class="brand"><span class="brand__dot"></span><span>Lora Becket</span></div>
    <p class="front__tagline">Psychotherapy &amp; Expressive Arts</p>
  </section>

  <section class="card card--back" aria-label="Card back">
    <div class="back__accent"></div>
    <header class="back__header">
      <h1 class="back__name">Lora Becket</h1>
      <p class="back__role">Counseling, Psychotherapy &amp; Expressive Arts</p>
    </header>
    <div class="back__mark" role="img" aria-label="Warm flame mark area"></div>
    <address class="back__contact">
      <div class="contact__line">
        <span>415.206.3791</span>
        <svg class="contact__icon" viewBox="0 0 10 10" aria-hidden="true">
          <rect x="2.5" y="0.5" width="5" height="9" rx="1" fill="none" stroke="var(--crimson)" stroke-width="1"/>
          <line x1="4" y1="8" x2="6" y2="8" stroke="var(--crimson)" stroke-width="0.8"/>
        </svg>
      </div>
      <div class="contact__line">
        <span>2914 Alderwood Avenue, Suite D</span>
        <svg class="contact__icon" viewBox="0 0 10 10" aria-hidden="true">
          <path d="M1 5 L5 1.2 L9 5 M2.3 4 V9 H7.7 V4 M4.2 9 V6.5 H5.8 V9" fill="none" stroke="var(--crimson)" stroke-width="1"/>
        </svg>
      </div>
      <div class="contact__line">
        <span>San Francisco, CA 94127</span>
        <svg class="contact__icon contact__icon--blank" viewBox="0 0 10 10" aria-hidden="true"></svg>
      </div>
      <div class="contact__line">
        <span>lorajanebecket@meadowpost.net</span>
        <svg class="contact__icon contact__icon--blank" viewBox="0 0 10 10" aria-hidden="true"></svg>
      </div>
      <div class="contact__line">
        <span>www.lorabecketmft.com</span>
        <svg class="contact__icon contact__icon--blank" viewBox="0 0 10 10" aria-hidden="true"></svg>
      </div>
      <div class="contact__line contact__license">
        <span>MFT License Number 48671</span>
        <svg class="contact__icon contact__icon--blank" viewBox="0 0 10 10" aria-hidden="true"></svg>
      </div>
    </address>
  </section>
</main>
</body>
</html>
```